R&T Cleanwave Stripping Business Card

We are in need of a business card design for our new Texas based company called 'R&T Cleanwave Stripping'. Our new innovative mobile media blasting service utilizes recycled material and a new water based process that eliminates all dust (i.e. as apposed to the old sand blasting format). Our 'advanced surface preparation' service targets multiple industries such as automotive, Industrial, marine and structural (graffiti removal). We would like to see the design include a recycling type logo or concept that utilizes colors such as black, various shades of green, some white, yellow and/or grey (e.g. perhaps a blackish background). The final design should look simple and professional and should clearly communicate the environmentally friendly approach through logo or design (i.e. Eco-Friendly, Go Green or Blast Green methodologies). Thank you in advance!
Updates

Please pardon any inconvenience. We have decided to pursue a two sided business card. All original information/designs requirements remains the same for the front. However, we would like back of the card to state the following: "We bring the power of Hydroveil Media Scouring equipment to your location. We can remove any coating from any surface. Bullets include: Paint Stripping, Auto Restoration, Graffiti Removal, Black Walls & Stone, Concrete, Boats, Iron Fences, Tractors & Trailers, Pools & Fountains, Wood Restoration.

Industry/Entity Type

Recycling

Contact Information for Business Card

R&T Cleanwave Stripping, LLC - Gordon Pelly, MBA, PMP - cell: 915-382-6091, office: 915-627-8853 - gpelly@rtcleanwavestripping.com - CEO/Founder

Requirements
Must have
• Recycle or environmentally friendly logos or design.
Nice to have
• Business oriented design with an aggressive look. Also, if possible would like to see R&T incorporated into the design or logo. Please note that we have decided to add the option of adding details to the back of the card (2 sided). The front should contain the logo/design and the back should have the following details listed: "We bring the power of Hydroveil Media Scouring equipment to your location. We can remove any coating from any surface. Bullets include: Paint Stripping, Auto Restoration, Graffiti Removal, Black Walls & Stone, Concrete, Boats, Iron Fences, Tractors & Trailers, Pools & Fountains, Wood Restoration.

```html
<!DOCTYPE html>
<html lang="en">
<head>
<meta charset="utf-8">
<title>R&amp;T Cleanwave Stripping – Business Card</title>
<link href="https://fonts.googleapis.com/css2?family=IBM+Plex+Sans:ital,wght@0,400;0,600;0,700;1,400&display=swap" rel="stylesheet">
<style>
  :root {
    --black: #000000;
    --board: #2a2a2a;
    --card-dark: #2b3134;
    --card-light: #f2f2f1;
    --ink: #2b3134;
    --white: #ffffff;
    --soft-white: #e6e6e6;
    --green: #3aa04a;
    --gold: #b3a33e;
    --gold-faint: rgba(179, 163, 62, 0.28);
  }
  * { box-sizing: border-box; margin: 0; padding: 0; }
  html, body { width: 1200px; height: 1000px; overflow: hidden; background: var(--black); }
  body { position: relative; font-family: "IBM Plex Sans", Arial, sans-serif; }

  .brand { display: flex; align-items: center; }
  .brand-dot { flex: none; border-radius: 50%; background: var(--green); }
  .brand-name { font-weight: 700; color: var(--white); white-space: nowrap; letter-spacing: -0.5px; }
  .brand-name .llc { font-size: 0.45em; vertical-align: 0.9em; margin-left: 4px; letter-spacing: 2px; }

  .masthead {
    position: absolute; left: 0; top: 0; width: 1200px; height: 155px;
    display: flex; align-items: center; justify-content: center;
  }
  .masthead .brand { gap: 26px; }
  .masthead .brand-dot { width: 92px; height: 92px; }
  .masthead .brand-name { font-size: 58px; }

  .board { position: absolute; left: 20px; top: 157px; width: 1160px; height: 823px; background: var(--board); }

  .card {
    position: absolute; left: 288px; width: 627px; height: 357px; border-radius: 22px;
    box-shadow: 0 2px 6px rgba(0,0,0,0.45); overflow: hidden;
  }
  .card-front { top: 193px; background: var(--card-dark); }
  .card-back { top: 590px; background: var(--card-light); }

  .card-front .brand { position: absolute; left: 46px; top: 88px; gap: 20px; }
  .card-front .brand-dot { width: 70px; height: 70px; }
  .card-front .brand-name { font-size: 36px; }

  .holder { position: absolute; right: 46px; top: 190px; text-align: right; }
  .holder-name { font-size: 26px; font-weight: 600; color: var(--soft-white); letter-spacing: 0.3px; }
  .holder-role { font-size: 17px; color: var(--green); margin-top: 2px; letter-spacing: 0.5px; }

  .contacts { position: absolute; right: 46px; top: 274px; text-align: right; color: var(--soft-white); font-size: 17px; line-height: 24px; letter-spacing: 0.4px; }
  .contact { display: inline-flex; align-items: center; gap: 7px; margin-left: 12px; }
  .contact svg { fill: var(--gold); }

  .back-mark {
    position: absolute; left: 38px; top: 30px; width: 300px; height: 300px;
    border-radius: 50%; background: var(--gold-faint);
  }
  .back-brand { position: absolute; left: 30px; width: 340px; top: 76px; display: flex; flex-direction: column; align-items: center; gap: 16px; }
  .back-brand .brand-dot { width: 64px; height: 64px; }
  .back-brand .brand-name { color: var(--ink); font-size: 27px; line-height: 36px; }
  .tagline { position: absolute; left: 30px; width: 340px; top: 210px; text-align: center; color: var(--ink); font-style: italic; }
  .tagline p { font-size: 16px; line-height: 25px; }
  .tagline p.small { font-size: 13px; line-height: 26px; }

  .services { position: absolute; left: 384px; top: 60px; color: var(--ink); }
  .services h2 { font-size: 17px; font-weight: 700; letter-spacing: 0.4px; margin-bottom: 20px; }
  .services ul { list-style: none; }
  .services li { font-size: 17.5px; line-height: 20px; position: relative; padding-left: 12px; }
  .services li::before { content: ""; position: absolute; left: 2px; top: 8px; width: 5px; height: 5px; border-radius: 50%; background: var(--green); }
</style>
</head>
<body>
  <header class="masthead">
    <div class="brand">
      <span class="brand-dot" aria-hidden="true"></span>
      <div class="brand-name">R&amp;T Cleanwave Stripping<span class="llc">LLC</span></div>
    </div>
  </header>

  <div class="board"></div>

  <section class="card card-front">
    <div class="brand">
      <span class="brand-dot" aria-hidden="true"></span>
      <div class="brand-name">R&amp;T Cleanwave Stripping<span class="llc">LLC</span></div>
    </div>
    <div class="holder">
      <div class="holder-name">Gordon Pelly</div>
      <div class="holder-role">CEO | Founder</div>
    </div>
    <div class="contacts">
      <div>
        <span class="contact">
          <svg width="10" height="14" viewBox="0 0 10 14" aria-hidden="true"><path d="M1.5 0h7A1.5 1.5 0 0 1 10 1.5v11A1.5 1.5 0 0 1 8.5 14h-7A1.5 1.5 0 0 1 0 12.5v-11A1.5 1.5 0 0 1 1.5 0zM1.8 1.8v9h6.4v-9z"/></svg>
          915-627-8853
        </span>
        <span class="contact">
          <svg width="15" height="13" viewBox="0 0 15 13" aria-hidden="true"><path d="M0 4C0 1 3 0 7.5 0S15 1 15 4l-3.5.6V3H3.5v1.6z"/><path d="M3 5h9l2 8H1zM7.5 7a2 2 0 1 0 0 4 2 2 0 0 0 0-4z"/></svg>
          915-382-6091
        </span>
      </div>
      <div>
        <span class="contact">
          <svg width="14" height="10" viewBox="0 0 14 10" aria-hidden="true"><path d="M0 0h14L7 5.5z"/><path d="M0 1.5l7 5.5 7-5.5V10H0z"/></svg>
          gpelly@rtcleanwavestripping.com
        </span>
      </div>
    </div>
  </section>

  <section class="card card-back">
    <div class="back-mark" role="img" aria-label="Faint eco emblem behind the company name"></div>
    <div class="back-brand">
      <span class="brand-dot" aria-hidden="true"></span>
      <div class="brand-name">R&amp;T Cleanwave Stripping<span class="llc">LLC</span></div>
    </div>
    <div class="tagline">
      <p>We bring the power of Hydroveil Media.</p>
      <p>Scouring equipment to your location.</p>
      <p class="small">We can remove any coating from any surface.</p>
    </div>
    <div class="services">
      <h2>BULLETS INCLUDE</h2>
      <ul>
        <li>Paint Stripping</li>
        <li>Auto Restoration</li>
        <li>Graffiti Removal</li>
        <li>Black Walls &amp; Stone</li>
        <li>Concrete</li>
        <li>Boats</li>
        <li>Iron Fences</li>
        <li>Tractors &amp; Trailers</li>
        <li>Pools &amp; Fountains</li>
        <li>Wood Restoration</li>
      </ul>
    </div>
  </section>
</body>
</html>
```